Lotvantage.com Webpage Design

Design Brief for lotvantage.com (Copy of Brief also in attached Word file)

Name of Website- lotvantage.com (existing logo and look & feel of website to be changed)

Logo - Finalised. The logo files are attached with the brief as “logo.jpeg”. The “Blue- Grey” version of the logo is for use on lighter backgrounds and the “Orange-White” version of the logo is for use on darker backgrounds. (A full Black version of the logo is also attached). Both versions may be used in different parts of the website. All attached files are in .png format.
Status - The website in functional and is undergoing user trials. However, we want to improve the look & feel of the website so at it seems
a. cotemporary,
b. Easy to Navigate
c. professional and
d. Vibrant.

Please visit ‘lotvantage.com’ to check out the website and its functionalities – please use it only as a reference for the features & functions to be provided, however the designer should use a ‘Free Hand’ in designing the composition of various parts of the webpage without getting too influenced by the existing design

Objective of the Website ‘lotvantage.com –
a. It is a portal focussed on listing of ‘Retail’ specific real-estate properties by developers, owners and realty brokers. The properties shall listed under the following four categories-
i. Retail Malls
ii. Shopping Complexes
iii. High-street shops
iv. Retail Warehouses
*refer lotvantage.com for better clarity

b. The abovementioned properties shall be listed either for ‘Sale’ or ‘rent\lease’ or both

c. Users shall visit the site in case they wish to acquire a retail \ shop space either on ‘sale’ or ‘rent’. These Users would be able to specify the ‘Search Criteria’ through the tool-bars provided on the website – the ‘Search Criteria’ shall comprise of ‘Type of space category’, ‘City’, ‘Locality’, transaction type ie ‘Rent \ Sale’ and ‘Area Range’

d. The main revenue model for the website shall be listing fee ( or advertising charges ) payable by those listing their properties on the website.

Three Main Pages of Website (lotvantage.com) that need to be designed -
a. Main Home Page (visit the web link - http://lotvantage.com/ ) - The main home page has the “Search Toolbar” for specifying of Search Criteria by the User. It shall also have the following features & functions-
i. Main Advertising Banner
ii. Featured Projects
iii. New Launches
iv. Toolbar with buttons – ‘Advertise with Us’, ‘Listings Alert’, ‘Lot Mavens’, ‘Advertiser Login’

b. Property Listings Page (visit the web link - http://lotvantage.com/gurgaon-in-india ) - The List of property options that match the Criteria specified by the ‘User’ get displayed on this page.

c. Property Detail Page - When the ‘User’ clicks on the “More….” Button on the ‘Property Listings Page’ (given in point b. above) the web page with the details of the property opens. (For Example – visit the web link - http://lotvantage.com/brevo-Shopping-Complex-brevo-quadrel-gurgaon-636 )

Note:- Please refer to attached ‘Shopping’ related images the designer may use them on the website to provide a look & feel of retail if required – either separately or rotate in a single window

Target Market(s)

Retailers & Investors looking for retail space, Real Estate Brokers, Developers

Industry/Entity Type

Advertising

Number of Pages Required

3 page

Requirements
Must have
• Refer to existing site lotvantage.com -- all the existing functionalities are a must have.
Nice to have
• The Designer may use the retail related images on the website if required for making it more vibrant. Refer attached images Shopping(1-6).jpg

```html
<!DOCTYPE html>
<html lang="en">
<head>
<meta charset="utf-8">
<title>Lotvantage.com – Home</title>
<link href="https://fonts.googleapis.com/css2?family=Open+Sans:wght@400;600;700&display=swap" rel="stylesheet">
<style>
:root{
  --dark:#2a2a2a;
  --orange:#f6b03c;
  --blue:#22618f;
  --text:#333;
  --line:#d8d8d8;
  --bg-soft:#f1f1f1;
  --white:#fff;
}
*{box-sizing:border-box;margin:0;padding:0}
html,body{width:1200px;height:2732px;overflow:hidden}
body{font-family:"Open Sans",Arial,sans-serif;color:var(--text);background:var(--white);position:relative}
.abs{position:absolute}

.topbar{left:0;top:0;width:1200px;height:102px;background:var(--dark)}
.brand{left:22px;top:22px;display:flex;align-items:center;gap:12px}
.brand-dot{width:40px;height:40px;border-radius:50%;background:var(--orange)}
.brand-name{font-size:32px;font-weight:700;color:var(--white);line-height:1}
.brand-tag{font-size:10px;font-weight:600;color:var(--white);letter-spacing:.5px;white-space:nowrap}
.city-pick{left:902px;top:12px;color:var(--white);font-size:16px;letter-spacing:1px}
.city-pick .select{margin-top:8px;width:276px;height:34px;background:var(--white);color:#555;font-size:12px;padding:8px 10px;position:relative;letter-spacing:0}
.city-pick .select:after{content:"";position:absolute;right:10px;top:14px;border:5px solid transparent;border-top-color:#555}

.mainnav{left:0;top:102px;width:1200px;height:103px;display:flex;padding:0 10px;background:var(--white)}
.navitem{flex:1;text-align:center;padding-top:28px;position:relative}
.navitem b{display:block;font-size:15px;font-weight:400;color:#222}
.navitem small{font-size:11px;color:#444}
.navitem:after{content:"";position:absolute;left:50%;transform:translateX(-50%);bottom:22px;width:112px;height:3px;background:var(--orange)}
.navitem.login:after{background:#222}
.navitem.register:after{background:var(--blue)}
.navitem.login b,.navitem.register b{font-weight:600;font-size:16px}
.navitem.login small,.navitem.register small{display:block;margin-bottom:2px}
.navitem.login:before,.navitem.register:before{content:"";position:absolute;left:0;top:22px;height:55px;border-left:1px solid var(--line)}

.hero-photo{left:0;top:205px;width:888px;height:365px;background:linear-gradient(120deg,#e9e2d8 0%,#d9c9b4 35%,#e88a2e 55%,#c9a983 75%,#efe6dc 100%)}
.hero-menu{left:888px;top:205px;width:312px;height:365px;background:#f2f2f2}
.hero-item{height:91px;border-bottom:1px solid #ddd;padding:22px 0 0 44px;position:relative}
.hero-item b{display:block;font-size:15px;font-weight:600;color:#333;letter-spacing:.3px}
.hero-item span{font-size:12px;color:#666}
.hero-item.active{background:var(--orange);margin-left:-22px;padding-left:66px}
.hero-item.active b,.hero-item.active span{color:var(--white)}
.hero-item .go{position:absolute;right:14px;top:27px;width:36px;height:36px;border:2px solid var(--white);border-radius:50%}

.search{left:0;top:570px;width:1200px;height:160px;background:var(--dark);color:var(--white);padding:0 22px}
.lookfor{display:flex;gap:34px;align-items:center;font-size:11px;font-weight:600;margin-top:33px}
.lookfor label{display:flex;align-items:center;gap:8px}
.lookfor i{width:11px;height:11px;background:var(--white);display:inline-block}
.fields{display:flex;gap:18px;margin-top:30px}
.field span{display:block;font-size:11px;font-weight:700;margin-bottom:6px}
.field .select,.field .input{height:28px;background:var(--white);color:#555;font-size:11px;padding:6px 8px;position:relative}
.field .select:after{content:"";position:absolute;right:0;top:0;width:22px;height:28px;background:var(--orange)}
.search-btn{width:90px;height:28px;background:var(--orange);font-size:12px;font-weight:700;text-align:center;line-height:28px;align-self:flex-end}

.listing{left:0;width:1200px}
.sec-title{position:relative;text-align:center;height:60px}
.sec-title h2{font-size:20px;font-weight:400;color:#222;letter-spacing:.5px}
.sec-title p{font-size:11px;color:#333}
.sec-title .rule{position:absolute;top:14px;height:1px;background:#bbb}
.arrow{position:absolute;top:4px;width:26px;height:18px;border:1px solid #9bb3c6;background:var(--white)}
.cards{display:flex;gap:34px;padding-left:23px;margin-top:26px}
.card{width:262px;height:349px;border:1px solid var(--line);background:var(--white);text-align:center}
.card.active{border-color:#9ec1dd}
.card h3{font-size:17px;font-weight:600;color:#222;padding:12px 0 10px;letter-spacing:.5px}
.card .thumb{margin:0 10px;height:128px;background:linear-gradient(180deg,#9cb3c9 0%,#b9a99a 55%,#7a6a5c 100%)}
.card .name{font-size:12px;color:#222;margin-top:18px;line-height:17px}
.card .kind{font-size:12px;font-weight:700;margin-top:2px}
.card hr{border:0;border-top:1px solid var(--line);margin:14px 20px 10px}
.btn{display:inline-block;border:1px solid var(--blue);color:var(--blue);font-size:11px;font-weight:600;padding:7px 14px;letter-spacing:.5px;background:var(--white)}
.card.active .btn{background:var(--blue);color:var(--white)}

.info{left:0;top:1753px;width:1200px;height:432px;display:flex;padding:0 44px}
.info-col{padding-top:32px}
.info-col h4{font-size:16px;font-weight:400;color:#222;letter-spacing:.5px;margin-bottom:14px}
.info-col p{font-size:12px;color:#444;line-height:19px}
.box{height:36px;border:1px solid #bbb;font-size:11px;padding:10px;color:#444;margin-top:10px;position:relative}
.box.select:after{content:"";position:absolute;right:10px;top:15px;border:5px solid transparent;border-top-color:#666}
.note{font-size:11px;color:#444;margin-top:12px}
.editor-thumb{width:246px;height:132px;background:linear-gradient(180deg,#a8bccf 0%,#b9a18b 60%,#6f5f52 100%);margin-bottom:12px}
.btn-solid{display:inline-block;background:var(--blue);color:var(--white);font-size:12px;font-weight:600;padding:9px 26px;margin-top:16px}

.about{left:0;top:2197px;width:1200px;height:285px;background:var(--bg-soft);text-align:center;padding-top:36px}
.about h5{font-size:20px;font-weight:700;color:#222}
.about p{width:1000px;margin:26px auto 0;font-size:13px;line-height:22px;color:#444}
.about .btn{margin-top:34px;padding:7px 58px;border-color:#777;color:#444}

.footer{left:0;top:2493px;width:1200px;height:239px;background:var(--dark);color:var(--white)}
.foot-about{left:50px;top:26px}
.foot-about h6,.foot-contact h6{font-size:15px;font-weight:700}
.foot-links{display:flex;gap:60px;margin-top:12px;font-size:13px}
.foot-links li{list-style:none;margin-bottom:9px;position:relative;padding-left:18px}
.foot-links li:before{content:"";position:absolute;left:0;top:5px;border:4px solid transparent;border-left:5px solid var(--white)}
.vrule{top:22px;width:1px;height:195px;background:#666}
.foot-center{left:420px;top:30px;width:360px;text-align:center}
.social{display:flex;justify-content:center;gap:26px}
.social i{width:18px;height:18px;border-radius:50%;background:var(--white)}
.foot-center hr{border:0;border-top:1px solid #777;margin:18px 0}
.foot-brand{display:flex;align-items:center;justify-content:center;gap:10px;font-size:30px;font-weight:700}
.foot-brand i{width:34px;height:34px;border-radius:50%;background:var(--orange)}
.foot-tag{font-size:9px;font-weight:600;letter-spacing:.5px;margin-top:4px}
.copy{font-size:11px;line-height:15px;margin-top:16px}
.foot-contact{left:890px;top:26px;font-size:13px;line-height:20px}
.foot-contact .row{display:flex;gap:10px;margin-top:10px}
</style>
</head>
<body>

<header class="abs topbar">
  <div class="abs brand">
    <span class="brand-dot"></span>
    <span class="brand-name">lotvantage.com</span>
  </div>
  <div class="abs brand-tag" style="left:74px;top:68px">INDIA'S LEADING PORTAL FOR RETAIL SPACE</div>
  <div class="abs city-pick">SELECT YOUR CITY:
    <div class="select">-Select-</div>
  </div>
</header>

<nav class="abs mainnav">
  <div class="navitem"><b>Advertise with us</b><small>Standard listing - FREE</small></div>
  <div class="navitem"><b>Lot Mavens</b><small>Shop Search Services</small></div>
  <div class="navitem"><b>Listing Alert</b><small>On the site live</small></div>
  <div class="navitem"><b>List Your Property Here</b><small>Watch the listing</small></div>
  <div class="navitem login"><small>Already Advertiser</small><b>Login Here</b></div>
  <div class="navitem register"><small>New Advertiser</small><b>Register Here</b></div>
</nav>

<div class="abs hero-photo" role="img" aria-label="Smiling shopper in an orange top holding colourful shopping bags"></div>
<aside class="abs hero-menu">
  <div class="hero-item"><b>RETAIL MALLS</b><span>Centrally Air-Conditioned</span></div>
  <div class="hero-item active"><b>SHOPPING COMPLEX</b><span>Non Air-Conditioned Building</span>
    <svg class="go" viewBox="0 0 36 36"><path d="M15 11l7 7-7 7" fill="none" stroke="#fff" stroke-width="3"/></svg>
  </div>
  <div class="hero-item"><b>HIGH STREET SHOPS</b><span>Road Facing Retail</span></div>
  <div class="hero-item"><b>REATAIL WAREHOUSESS</b><span>Centrally Air-Conditioned</span></div>
</aside>

<section class="abs search">
  <div class="lookfor">
    <span>ARE YOU LOOKING FOR</span>
    <label><i></i>RETAIL MALLS</label>
    <label><i></i>SHOPPING COMPLEX</label>
    <label><i></i>HIGH STREET SHOPS</label>
    <label><i></i>RETAIL WAREHOUSES</label>
  </div>
  <div class="fields">
    <div class="field" style="width:242px"><span>SALE OR RENT OR BOTH:</span><div class="select">-Select-</div></div>
    <div class="field" style="width:242px"><span>SELECT CITY:</span><div class="select">-Select-</div></div>
    <div class="field" style="width:242px"><span>SELECT LOCALITY/MICRO-MARKET</span><div class="select">-Select</div></div>
    <div class="field" style="width:250px"><span>ENTER KEYWORDS</span><div class="input">Project name, Developers</div></div>
    <div class="search-btn">SEARCH</div>
  </div>
</section>

<section class="abs listing" style="top:760px">
  <div class="sec-title">
    <span class="arrow" style="left:23px"></span><span class="rule" style="left:70px;width:360px"></span>
    <h2>FEATURED RETAIL PROJECTS</h2><p>ACROSS INDIA</p>
    <span class="rule" style="right:70px;width:360px"></span><span class="arrow" style="right:23px"></span>
  </div>
  <div class="cards">
    <div class="card active"><h3>NOIDA</h3><div class="thumb" role="img" aria-label="Mall building exterior"></div><div class="name">ARVEN SKYLINE MALL<br>AMINJIKARAI</div><div class="kind">SHOPPING COMPLEX</div><hr><span class="btn">› VIEW THE LISTING</span></div>
    <div class="card"><h3>SURAT</h3><div class="thumb" role="img" aria-label="Glass-fronted high street building"></div><div class="name">NORVEL 81 HIGH STREET<br>SECTOR-81</div><div class="kind">RETAIL MALLS</div><hr><span class="btn">› VIEW THE LISTING</span></div>
    <div class="card"><h3>FARIDABAD</h3><div class="thumb" role="img" aria-label="Modern retail complex facade"></div><div class="name">K4K METROPOLITAN<br>SECTOR-65</div><div class="kind">SHOPPING COMPLEX</div><hr><span class="btn">› VIEW THE LISTING</span></div>
    <div class="card"><h3>GURGAON</h3><div class="thumb" role="img" aria-label="Mall front lit at dusk"></div><div class="name">MERIDIAN MALL-TAGORE GARDEN<br>TAGORE GARDEN</div><div class="kind">RETAIL MALLS</div><hr><span class="btn">› VIEW THE LISTING</span></div>
  </div>
</section>

<div class="abs" style="left:0;top:1252px;width:1200px;height:480px;background:var(--bg-soft)"></div>
<section class="abs listing" style="top:1283px">
  <div class="sec-title">
    <span class="arrow" style="left:23px"></span><span class="rule" style="left:70px;width:370px"></span>
    <h2>FEATURED NEW LAUNCHES</h2><p>ACROSS INDIA</p>
    <span class="rule" style="right:70px;width:370px"></span><span class="arrow" style="right:23px"></span>
  </div>
  <div class="cards">
    <div class="card active"><h3>NOIDA</h3><div class="thumb" role="img" aria-label="Mall building exterior"></div><div class="name">ARVEN SKYLINE MALL<br>AMINJIKARAI</div><div class="kind">SHOPPING COMPLEX</div><hr><span class="btn">› VIEW THE LISTING</span></div>
    <div class="card"><h3>SURAT</h3><div class="thumb" role="img" aria-label="Glass-fronted high street building"></div><div class="name">NORVEL 81 HIGH STREET<br>SECTOR-81</div><div class="kind">RETAIL MALLS</div><hr><span class="btn">› VIEW THE LISTING</span></div>
    <div class="card"><h3>FARIDABAD</h3><div class="thumb" role="img" aria-label="Modern retail complex facade"></div><div class="name">K4K METROPOLITAN<br>SECTOR-65</div><div class="kind">SHOPPING COMPLEX</div><hr><span class="btn">› VIEW THE LISTING</span></div>
    <div class="card"><h3>GURGAON</h3><div class="thumb" role="img" aria-label="Mall front lit at dusk"></div><div class="name">MERIDIAN MALL-TAGORE GARDEN<br>TAGORE GARDEN</div><div class="kind">RETAIL MALLS</div><hr><span class="btn">› VIEW THE LISTING</span></div>
  </div>
</section>

<section class="abs info">
  <div class="info-col" style="width:320px">
    <h4>LISTING ALERT</h4>
    <p>Suscribe for Fortnightly Email update<br>on New Listings @ Lotvantage</p>
    <div class="box" style="border-color:#8fb3d3;margin-top:14px">Enter email address</div>
    <div class="note">(select retail format of interest)</div>
    <div class="box select" style="margin-top:6px">Select options</div>
    <div class="note">(select cities of interest)</div>
    <div class="box select" style="margin-top:6px">Select city</div>
    <span class="btn-solid">SUBSCRIBE</span>
  </div>
  <div class="info-col" style="margin-left:102px;width:300px">
    <h4>EDITOR'S CHOICE</h4>
    <div class="editor-thumb" role="img" aria-label="Featured mall building exterior"></div>
    <p>A "Select" Listing of Retail Properties Handpicked by our Editors based on their own positive evaluation on parameters &amp; attributes such as Design Concept, Location, Developer, Success Potential. So Read On to Check Out for yourself</p>
    <span class="btn" style="margin-top:14px;padding:7px 50px;border-color:#8aa;color:#444">MORE</span>
  </div>
  <div class="info-col" style="margin-left:72px;width:316px">
    <h4>LOT MAVENS</h4>
    <p>Post your Retail Space requirement with us and our experts shall get back with suitable options and even help you in your transaction.</p>
    <div class="box" style="margin-top:12px">Enter email address</div>
    <div class="box" style="margin-top:14px">Mobile</div>
    <div class="box" style="margin-top:14px;height:90px">Add Description of Requirement</div>
    <span class="btn" style="margin-top:14px;padding:7px 50px;border-color:#8aa;color:#444">SEND</span>
  </div>
</section>

<section class="abs about">
  <h5>www.lotvantage.com</h5>
  <p>Lotvantage.com - About Us Lotvantage.com is a Specialised Web based platform for Retail Space, featuring properties across India under various formats such as Retail Malls, Shopping Complexes, High-street Shops. Also featured are Retail Warehouses which provide the logistic back-end for the retail business. Lotvantage.com is useful to various category of users as follows- a. Devel More...</p>
  <span class="btn">MORE</span>
</section>

<footer class="abs footer">
  <div class="abs foot-about">
    <h6>About Shopfront Central</h6>
    <div class="foot-links">
      <ul><li>About Us</li><li>Privacy Policy</li><li>Terms of Use</li><li>Contact Us</li><li>Site Map</li></ul>
      <ul><li>Retail Malls</li><li>Shopping Complex</li><li>High Street Shops</li><li>Retail Warehouses</li></ul>
    </div>
  </div>
  <span class="abs vrule" style="left:418px"></span>
  <div class="abs foot-center">
    <div class="social"><i></i><i></i><i></i><i></i></div>
    <hr>
    <div class="foot-brand"><i></i>lotvantage.com</div>
    <div class="foot-tag">INDIA'S LEADING PORTAL FOR RETAIL SPACE</div>
    <div class="copy">Copyright © 2013 Indus Shopfront Group.<br>All rights reserved.</div>
  </div>
  <span class="abs vrule" style="left:806px"></span>
  <div class="abs foot-contact">
    <h6>Contact</h6>
    <div class="row">
      <svg width="12" height="16" viewBox="0 0 12 16"><path d="M6 0a6 6 0 0 0-6 6c0 4.5 6 10 6 10s6-5.5 6-10a6 6 0 0 0-6-6zm0 8.5A2.5 2.5 0 1 1 6 3.5a2.5 2.5 0 0 1 0 5z" fill="#fff"/></svg>
      <div>Shopfront Central, Suite 212, 2nd Floor,<br>Lorem Ipsum is simply,<br>Block-y, Riverton - 560117</div>
    </div>
    <div class="row" style="margin-top:12px">
      <svg width="14" height="14" viewBox="0 0 14 14"><path d="M3 0l2.5 3.5-1.5 1.5c1 2 2.5 3.5 4.5 4.5l1.5-1.5L14 10.5 12 14C5.5 13.5.5 8.5 0 2z" fill="#fff"/></svg>
      <div>Phone : 000-000-0000</div>
    </div>
    <div class="row" style="margin-top:6px">
      <svg width="14" height="14" viewBox="0 0 14 14"><rect x="3" y="0" width="8" height="4" fill="#fff"/><rect x="0" y="5" width="14" height="6" fill="#fff"/><rect x="3" y="9" width="8" height="5" fill="#fff"/></svg>
      <div>Fax : 000 - 000 - 000</div>
    </div>
  </div>
</footer>

</body>
</html>
```